we do all sorts of cleaning however bookings are limited!
why not chose the right cleaners for you!
pressure cleaning, window cleaning, office, end of lease clean, accommodation, industrial and commercial cleaning and house cleaning

Logo Text

Bright Nest Cleaning Service

```html
<!DOCTYPE html>
<html lang="en">
<head>
<meta charset="utf-8">
<title>Bright Nest Cleaning Service – Business Card</title>
<link rel="stylesheet" href="https://fonts.googleapis.com/css2?family=Montserrat:wght@400;500;600;700&display=swap">
<style>
  :root {
    --bg: #2b2b2d;
    --card: #161617;
    --card-edge: #0c0c0d;
    --blue: #2ea3dd;
    --green: #7cc242;
    --white: #f2f2f2;
    --silver: #d8d8d8;
    --muted: #e6e6e6;
  }
  * { box-sizing: border-box; margin: 0; padding: 0; }
  html, body {
    width: 1200px; height: 900px; overflow: hidden;
    background: var(--bg);
    font-family: "Montserrat", sans-serif;
  }
  .stage {
    width: 1200px; height: 900px;
    display: flex; flex-direction: column;
    align-items: center; justify-content: center;
    gap: 56px;
  }
  .card {
    width: 630px; height: 360px;
    background: var(--card);
    border-radius: 22px;
    box-shadow: 0 6px 0 var(--card-edge), 0 18px 40px rgba(0,0,0,.45);
    position: relative;
    overflow: hidden;
  }

  /* Front */
  .card--front {
    display: flex; align-items: center; justify-content: center;
  }
  .front-mark {
    display: flex; flex-direction: column; align-items: center; gap: 10px;
    color: var(--silver);
    font-weight: 600;
  }
  .front-mark .dot {
    width: 18px; height: 18px; border-radius: 50%;
    background: var(--silver);
  }
  .front-mark .name { font-size: 50px; letter-spacing: .5px; line-height: 1; }
  .front-mark .tag { font-size: 18px; letter-spacing: 4px; text-transform: uppercase; }

  /* Back */
  .card--back {
    display: grid;
    grid-template-columns: 290px 2px 1fr;
    align-items: center;
    padding: 0 36px;
  }
  .back-mark {
    color: var(--blue);
    font-weight: 600;
    display: flex; flex-direction: column; align-items: flex-start; gap: 6px;
  }
  .back-mark .name { font-size: 32px; line-height: 1.05; }
  .back-mark .tag { font-size: 12px; letter-spacing: 2px; text-transform: uppercase; }
  .divider {
    width: 2px; height: 200px; background: var(--green);
  }
  .details { padding-left: 30px; color: var(--muted); }
  .person { font-size: 25px; font-weight: 700; line-height: 1.1; }
  .person .first { color: var(--blue); }
  .person .last { color: var(--green); }
  .role { font-size: 14px; margin-top: 4px; }
  .address { font-size: 14px; margin-top: 14px; line-height: 1.45; }
  .contacts { list-style: none; margin-top: 10px; font-size: 14px; }
  .contacts li { display: flex; align-items: center; gap: 10px; line-height: 1.7; }
  .contacts svg { width: 13px; height: 13px; fill: var(--green); flex: none; }
</style>
</head>
<body>
<main class="stage">
  <section class="card card--front">
    <div class="front-mark">
      <span class="dot"></span>
      <span class="name">Bright Nest</span>
      <span class="tag">Cleaning Service</span>
    </div>
  </section>

  <section class="card card--back">
    <div class="back-mark">
      <span class="name">Bright Nest</span>
      <span class="tag">Cleaning Service</span>
    </div>
    <span class="divider"></span>
    <div class="details">
      <p class="person"><span class="first">Daniel</span> <span class="last">Harper</span></p>
      <p class="role">Managing Director</p>
      <p class="address">Your address, City<br>State, Zip 1234</p>
      <ul class="contacts">
        <li>
          <svg viewBox="0 0 24 24"><path d="M6.6 10.8a15.1 15.1 0 0 0 6.6 6.6l2.2-2.2a1 1 0 0 1 1-.25 11.4 11.4 0 0 0 3.6.57 1 1 0 0 1 1 1V20a1 1 0 0 1-1 1A17 17 0 0 1 3 4a1 1 0 0 1 1-1h3.5a1 1 0 0 1 1 1c0 1.25.2 2.45.57 3.57a1 1 0 0 1-.25 1z"/></svg>
          123 456 789
        </li>
        <li>
          <svg viewBox="0 0 24 24"><path d="M2 5h20v14H2z M3 6l9 7 9-7" /></svg>
          info@yourmail.com
        </li>
        <li>
          <svg viewBox="0 0 24 24"><circle cx="12" cy="12" r="10"/></svg>
          www.yourwebsite.com
        </li>
      </ul>
    </div>
  </section>
</main>
</body>
</html>
```